Birthday Party Invitation

I need to create a "save the date" for my birthday party.
Text:

Save the Date
Saturday, 6 December 2014
9 pm
Club la Vereda, Lindenhofweg 42, 8005 Zürich
BLACK IT OUT
SAVE IT!
RESERVE THE TIME
WRITE IT DOWN
HOLD THE DATE to LET YOUR HAIR DOWN and Party with Me.

Target Market(s)

Friends

Industry/Entity Type

Club

Requirements
Must have
• I want the flyer to look classy and sexy at the same time.
Nice to have
• Picture on the left or right, then text white on black background. Maybe a simple frame. Not too playful, rather simple, elegant and no graphics. Just picture and text.

```html
<!DOCTYPE html>
<html lang="en">
<head>
<meta charset="utf-8">
<title>Save the Date – Birthday Party Invitation</title>
<link rel="stylesheet" href="https://fonts.googleapis.com/css2?family=Titillium+Web:wght@300;400&display=swap">
<style>
  :root {
    --stage: #e4e7e7;
    --paper: #ffffff;
    --night: #050505;
    --ink: #f4f4f4;
    --accent: #e0100f;
    --photo-dark: #120a08;
    --photo-warm: #5a2a1a;
    --photo-red: #9c1420;
    --photo-fur: #e8e2d8;
  }
  html, body {
    margin: 0;
    width: 1200px;
    height: 1000px;
    overflow: hidden;
    background: var(--stage);
  }
  .canvas {
    position: relative;
    width: 1200px;
    height: 1000px;
  }
  .invitation {
    position: absolute;
    left: 100px;
    top: 125px;
    width: 1000px;
    height: 750px;
    display: flex;
    box-shadow: 0 6px 24px rgba(0,0,0,0.18);
  }
  .invitation__photo-side {
    position: relative;
    width: 500px;
    height: 100%;
    background: var(--paper);
  }
  .portrait {
    position: absolute;
    left: 85px;
    top: 115px;
    right: 0;
    bottom: 60px;
    background:
      radial-gradient(ellipse 55% 35% at 45% 20%, var(--photo-fur) 0%, rgba(232,226,216,0) 60%),
      radial-gradient(ellipse 55% 45% at 50% 70%, var(--photo-red) 0%, rgba(156,20,32,0) 70%),
      radial-gradient(ellipse 80% 70% at 40% 45%, var(--photo-warm) 0%, var(--photo-dark) 75%);
  }
  .invitation__text-side {
    position: relative;
    width: 500px;
    height: 100%;
    background: var(--night);
  }
  .frame {
    position: absolute;
    inset: 0;
  }
  .details {
    position: absolute;
    left: 45px;
    top: 108px;
    margin: 0;
    color: var(--ink);
    font-family: "Titillium Web", sans-serif;
    font-weight: 300;
    font-size: 27px;
    line-height: 30px;
  }
  .details p { margin: 0; }
  .details .call-to-action {
    margin-top: 28px;
    padding-left: 12px;
  }
</style>
</head>
<body>
<div class="canvas">
  <article class="invitation">
    <section class="invitation__photo-side">
      <div class="portrait" role="img" aria-label="Photograph of the host in a red velvet Santa dress with white fur trim and hat, against a dark background"></div>
    </section>
    <section class="invitation__text-side">
      <svg class="frame" width="500" height="750" viewBox="0 0 500 750">
        <g fill="none" stroke="var(--accent)" stroke-width="2">
          <line x1="0" y1="78" x2="395" y2="78"/>
          <line x1="430" y1="110" x2="430" y2="640"/>
          <line x1="0" y1="692" x2="395" y2="692"/>
        </g>
        <rect x="385" y="45" width="80" height="70" fill="var(--accent)" opacity="0.85" role="img" aria-label="Red floral corner flourish"/>
        <rect x="395" y="635" width="80" height="70" fill="var(--accent)" opacity="0.85" role="img" aria-label="Red floral corner flourish"/>
      </svg>
      <div class="details">
        <p class="event-info">Save the Date<br>
          Saturday, 6 December 2014<br>
          9 pm<br>
          Club la Vereda,<br>
          Lindenhofweg 42,<br>
          8005 Zürich</p>
        <p class="call-to-action">BLACK IT OUT<br>
          SAVE IT !<br>
          RESERVE THE TIME<br>
          WRITE IT DOWN<br>
          HOLD THE DATE to<br>
          LET YOUR HAIR DOWN and<br>
          Party with Me.</p>
      </div>
    </section>
  </article>
</div>
</body>
</html>
```